Leadership Brenvale Brochure Design*

We host a local leadership development program every two years. We need a brochure to promote the program. We would like it to be 8 1/2 x 11, tri-fold. I have attached a Word document with the necessary info for the brochure. The brochure will be professionally printed. We would like the final design to be in InDesign.

Target Market(s)

Potential participants of our leadership program. They will be local leaders, male and female, from 30-60 years of age.

Requirements
Must have
• Content as detailed in the Word document attached. Our logo.
Nice to have
• A design that is attractive to young professionals.

```html
<!DOCTYPE html>
<html lang="en">
<head>
<meta charset="utf-8">
<title>Leadership Brenvale – Brochure Inside Spread</title>
<link rel="stylesheet" href="https://fonts.googleapis.com/css2?family=Lato:wght@400;700&family=Libre+Franklin:wght@800&family=Source+Serif+4:wght@400;600&display=swap">
<style>
  :root{
    --sky:#7ac6ec;
    --navy:#3a4796;
    --green:#3fb452;
    --orange:#f08a2c;
    --ink:#231f20;
    --paper:#ffffff;
  }
  *{margin:0;padding:0;box-sizing:border-box}
  html,body{width:1200px;height:933px;overflow:hidden;background:var(--paper)}
  .spread{position:relative;width:1200px;height:933px;overflow:hidden;font-family:"Lato",sans-serif;color:var(--ink)}
  .backdrop{position:absolute;inset:0}
  .block{position:absolute;font-size:14.4px;line-height:20.7px}
  .section-title{color:var(--green);font-weight:400;font-size:16.5px;letter-spacing:.4px;margin-bottom:9px;line-height:20px}
  .alumni-heading{position:absolute;left:503px;top:52px;color:#fff;font-family:"Source Serif 4",serif;font-size:23px;line-height:31px}
  .role{font-weight:700;font-size:14.4px;line-height:20.7px}
  .quote{margin-top:12px}
  .contact{position:absolute;left:50px;top:806px;width:322px;text-align:right;font-weight:700;font-size:15.6px;line-height:20.5px}
  .portrait{position:absolute;border-radius:50%;background:radial-gradient(circle at 50% 40%,#b9b9b9,#6d6d6d 70%,#4a4a4a)}
  .portrait-ring{position:absolute;border-radius:50%;background:#fff}
  .brand{position:absolute;left:858px;top:112px;display:flex;align-items:center;gap:10px}
  .brand-dot{width:38px;height:38px;border-radius:50%;background:var(--green)}
  .brand-name{font-family:"Libre Franklin",sans-serif;font-weight:800;color:var(--navy);font-size:27px;line-height:29px;letter-spacing:-.3px}
  .motto{position:absolute;left:830px;top:586px;font-family:"Source Serif 4",serif;font-weight:600;font-size:26px;line-height:32.6px}
  .motto .warm{color:var(--orange)}
  .motto .cool{color:var(--navy)}
  .sponsors{position:absolute;left:830px;top:820px}
  .sponsors .section-title{font-size:15px;margin-bottom:10px}
  .sponsors p{font-weight:700;font-size:14.6px;line-height:20.8px}
</style>
</head>
<body>
<main class="spread">
  <svg class="backdrop" width="1200" height="933" viewBox="0 0 1200 933">
    <rect x="0" y="0" width="797" height="160" fill="var(--sky)"/>
    <path d="M0,128 C250,62 550,24 797,28 L797,235 C700,150 500,98 300,110 C180,118 80,134 0,153 Z" fill="var(--navy)"/>
    <path d="M0,822 C200,878 500,905 797,900 L797,933 L0,933 Z" fill="var(--green)"/>
    <path d="M797,313 C900,266 1050,246 1200,250 L1200,272 C1050,264 900,282 797,320 Z" fill="var(--sky)"/>
    <path d="M797,320 C900,282 1050,264 1200,272 L1200,578 C1100,530 960,506 797,522 Z" fill="url(#groupTone)" role="img" aria-label="Group photo of program alumni standing together indoors"/>
    <path d="M797,522 C960,506 1100,530 1200,578 L1200,588 C1100,556 950,546 797,560 Z" fill="var(--green)"/>
    <defs>
      <linearGradient id="groupTone" x1="0" y1="0" x2="1" y2="1">
        <stop offset="0" stop-color="#c9ab84"/>
        <stop offset=".5" stop-color="#a27a5c"/>
        <stop offset="1" stop-color="#5e4a48"/>
      </linearGradient>
    </defs>
  </svg>

  <h2 class="alumni-heading">What Community<br>alumni are saying</h2>

  <section class="block" style="left:50px;top:156px">
    <h3 class="section-title">ATTENDANCE POLICY</h3>
    <p>Attendance at all sessions including the opening<br>retreat is compulsory.&nbsp; Participants may miss no<br>more than one session to graduate; however, the<br>Organizational Retreat is mandatory.</p>
  </section>

  <section class="block" style="left:50px;top:311px">
    <h3 class="section-title">TUITION</h3>
    <p>If accepted in the Leadership Brenvale program,<br>you or your employer/sponsor will be invoiced<br>$400 for Chamber members and $500 for<br>non-members.&nbsp; This fee covers costs for the<br>retreat, classroom sessions, lunches, and<br>graduation.&nbsp; No refunds will be provided for<br>participants who drop out of the program or do<br>not fulfill the required curriculum.</p>
  </section>

  <section class="block" style="left:50px;top:543px">
    <h3 class="section-title">TO APPLY</h3>
    <p>Applications are available on the Chamber’s<br>website, www.TheBrenvaleChamber.com<br>Applications are due by November 2, 2020.<br>Class size is limited.&nbsp; All applications received by<br>the deadline will be reviewed and final<br>participants for the Leadership Brenvale class<br>will be contacted on December 4, 2020.&nbsp; However,<br>all applicants will be notified of the status of their<br>application in writing.</p>
  </section>

  <p class="contact">For questions, please call the Chamber,<br>910-555-0147.</p>

  <div class="portrait-ring" style="left:655px;top:135px;width:104px;height:104px"></div>
  <div class="portrait" role="img" aria-label="Portrait of Dana Whitfield" style="left:662px;top:142px;width:90px;height:90px"></div>

  <section class="block" style="left:429px;top:156px">
    <h3 class="section-title" style="margin-bottom:2px">DANA WHITFIELD</h3>
    <p class="role">Co-Owner, Hank’s Smokehouse</p>
    <p class="quote">“Leadership Brenvale was an<br>&nbsp;awesome experience! I learned<br>many interesting things about the county that I<br>have lived in all my life. We had very informative<br>panel discussions and the tours of local attractions,<br>including the Ashby Ridge Correctional Facility were<br>eye opening! I enjoyed learning and working beside<br>a great group of folks who are taking leadership<br>roles in our communities to make our county a<br>better place to live, work and play.”</p>
  </section>

  <div class="portrait-ring" style="left:424px;top:448px;width:84px;height:84px;border:1.5px solid var(--green)"></div>
  <div class="portrait" role="img" aria-label="Portrait of Owen R. Talley" style="left:430px;top:454px;width:72px;height:72px"></div>

  <section class="block" style="left:540px;top:444px">
    <h3 class="section-title" style="margin-bottom:6px">OWEN R. TALLEY</h3>
    <p class="role">CPA, Partner/Manager&nbsp; of the<br>Fairhollow Office, R. Calder<br>Wynn &amp; Associates, LLP</p>
  </section>

  <section class="block" style="left:429px;top:549px">
    <p>“For the first year and a half I was working at R.<br>Calder Wynn, I commuted from Marsh Point, so I<br>was not involved in the community at all. Once we<br>moved here, I knew I wanted and felt I had to become<br>more involved. I learned about the program through a<br>colleague.&nbsp; I couldn’t have asked for a better<br>experience and it really exposed me to the many ways<br>that I could get involved and contribute to the<br>chamber and our community.&nbsp; I didn’t know a soul in<br>that 2014 class when it started and now many of<br>them are my very best friends. If you have an<br>opportunity to go through Leadership Brenvale you<br>would be crazy to pass it up. It is the best program the<br>Chamber has and, quite frankly, one of the best<br>opportunities to better yourself in this community.</p>
  </section>

  <div class="brand">
    <span class="brand-dot"></span>
    <span class="brand-name">LEADERSHIP<br>BRENVALE</span>
  </div>

  <p class="motto">
    <span class="warm">The greatest wealth of a<br>community lies</span><br>
    <span class="cool">not in the amount of<br>its treasure, but</span><br>
    <span class="warm">in the quality<br>of its leadership</span>
  </p>

  <section class="sponsors">
    <h3 class="section-title">SPONSORED BY</h3>
    <p>Coastal Plains Community College<br>Brenvale Chamber of Commerce and Tourism</p>
  </section>
</main>
</body>
</html>
```